Brochure for medical doctor

I need a brochure for a medical doctor to promote his practice. The brochure should contain his picture, business information (use letterhead from attachment), and the following text:

- Now accepting PI cases on lien!
- Same and next business day appointments available for initial visits, pre-operative clearances, and all other medical needs

- Expedited medical reports sent quickly to your office

Medical

```html
<!DOCTYPE html>
<html lang="en">
<head>
<meta charset="utf-8">
<title>Meadowlane Medical Center</title>
<link href="https://fonts.googleapis.com/css2?family=Poppins:wght@400;600;700&display=swap" rel="stylesheet">
<style>
  :root {
    --green: #65a843;
    --yellow: #e8dc3a;
    --yellow-soft: #f3ea7a;
    --ink: #2b2b2b;
    --paper: #fbfbfb;
    --white: #ffffff;
  }
  * { margin: 0; padding: 0; box-sizing: border-box; }
  html, body { width: 842px; height: 1200px; overflow: hidden; background: var(--paper); }
  .flyer {
    position: relative;
    width: 842px; height: 1200px;
    overflow: hidden;
    background: var(--paper);
    font-family: "Poppins", sans-serif;
    color: var(--ink);
  }
  .decor { position: absolute; left: 0; top: 0; width: 842px; height: 1200px; }

  .brand-mark {
    position: absolute; left: 200px; top: 96px;
    width: 112px; height: 112px;
    background: var(--green);
  }
  .brand-name {
    position: absolute; left: 344px; top: 50px;
    font-family: "Poppins", sans-serif;
    font-weight: 700;
    font-size: 50px;
    line-height: 67px;
    color: var(--green);
    letter-spacing: 0.5px;
  }

  .portrait {
    position: absolute; left: 215px; top: 282px;
    width: 432px; height: 727px;
    border-radius: 190px 190px 0 0;
    background: linear-gradient(180deg, #e9e4e1 0%, #f2f2f2 30%, #e6e6e6 100%);
  }

  .bubble-text {
    position: absolute;
    text-align: center;
    font-weight: 700;
    text-transform: uppercase;
    color: var(--white);
  }
  .bubble-lien { left: 62px; top: 491px; width: 200px; font-size: 17.5px; line-height: 22.3px; }
  .bubble-reports { left: 580px; top: 557px; width: 220px; font-size: 17.5px; line-height: 22px; }
  .bubble-appointments { left: 116px; top: 787px; width: 300px; font-size: 16.6px; line-height: 21.5px; }

  .cta {
    position: absolute; left: 152px; top: 1082px;
    font-weight: 700; font-size: 23px; line-height: 30px;
  }
  .contact-line {
    position: absolute; font-size: 15px; line-height: 22px; color: var(--ink);
  }
  .contact-address { left: 541px; top: 1038px; }
  .contact-phone { left: 540px; top: 1092px; font-size: 13.5px; }
  .contact-fax { left: 540px; top: 1138px; font-size: 13.5px; }
</style>
</head>
<body>
<main class="flyer">
  <svg class="decor" viewBox="0 0 842 1200" aria-hidden="true">
    <defs>
      <linearGradient id="sunGlow" x1="0.2" y1="0.15" x2="0.8" y2="0.9">
        <stop offset="0" stop-color="#ffffff"/>
        <stop offset="0.45" stop-color="#fbf6c8"/>
        <stop offset="1" stop-color="#ecdf3c"/>
      </linearGradient>
    </defs>
    <circle cx="424" cy="693" r="316" fill="url(#sunGlow)"/>
    <g fill="none" stroke="var(--yellow)" stroke-width="2">
      <circle cx="86" cy="76" r="18"/>
      <circle cx="739" cy="250" r="18"/>
      <circle cx="166" cy="943" r="17"/>
    </g>
    <g fill="var(--yellow)">
      <rect x="118" y="265" width="24" height="6" rx="3"/><rect x="127" y="256" width="6" height="24" rx="3"/>
      <rect x="733" y="903" width="33" height="7" rx="3.5"/><rect x="746" y="890" width="7" height="33" rx="3.5"/>
      <rect x="148" y="1140" width="24" height="6" rx="3"/><rect x="157" y="1131" width="6" height="24" rx="3"/>
    </g>
  </svg>

  <div class="brand-mark" aria-hidden="true"></div>
  <h1 class="brand-name">MEADOWLANE<br>MEDICAL<br>CENTER</h1>

  <div class="portrait" role="img" aria-label="Photo of a doctor in a white coat with a stethoscope and face mask"></div>

  <svg class="decor" viewBox="0 0 842 1200" aria-hidden="true">
    <g fill="var(--green)">
      <!-- lien cloud -->
      <g>
        <circle cx="190" cy="525" r="65"/>
        <circle cx="118" cy="545" r="55"/>
        <circle cx="86" cy="545" r="46"/>
        <circle cx="235" cy="555" r="48"/>
        <circle cx="160" cy="570" r="38"/>
        <rect x="40" y="545" width="240" height="40" rx="20"/>
      </g>
      <!-- reports cloud -->
      <g>
        <circle cx="712" cy="600" r="68"/>
        <circle cx="640" cy="580" r="50"/>
        <circle cx="760" cy="620" r="44"/>
        <circle cx="622" cy="625" r="46"/>
        <circle cx="690" cy="650" r="40"/>
        <rect x="576" y="610" width="226" height="54" rx="27"/>
      </g>
      <!-- appointments cloud -->
      <g>
        <circle cx="296" cy="830" r="80"/>
        <circle cx="200" cy="825" r="55"/>
        <circle cx="370" cy="875" r="60"/>
        <circle cx="165" cy="880" r="60"/>
        <circle cx="262" cy="910" r="60"/>
        <rect x="105" y="850" width="323" height="80" rx="40"/>
      </g>
    </g>
  </svg>

  <p class="bubble-text bubble-lien">Now<br>accepting<br>PI cases<br>on lien!</p>
  <p class="bubble-text bubble-reports">Expedited<br>medical<br>reports sent<br>quickly to<br>your office</p>
  <p class="bubble-text bubble-appointments">Same and next<br>business day<br>appointments<br>available for initial visits,<br>pre-operative clearances,<br>and all other<br>medical needs</p>

  <svg class="decor" viewBox="0 0 842 1200" aria-hidden="true">
    <g stroke="var(--ink)" stroke-width="1.2" fill="none">
      <line x1="369" y1="1100" x2="467" y2="1100"/>
      <polyline points="488,1048 467,1048 467,1166 488,1166"/>
    </g>
    <g fill="var(--ink)">
      <!-- pin -->
      <path d="M516 1040 a8 8 0 0 1 8 8 c0 6 -8 15 -8 15 c0 0 -8 -9 -8 -15 a8 8 0 0 1 8 -8 z M516 1045 a3 3 0 1 0 0.01 0 z" fill-rule="evenodd"/>
      <!-- phone -->
      <path d="M506 1094 c2 -2 5 -2 6 0 l3 4 c1 2 0 3 -1 4 l-2 2 c2 4 5 7 9 9 l2 -2 c1 -1 3 -2 4 -1 l4 3 c2 1 2 4 0 6 l-2 2 c-8 2 -24 -14 -23 -23 z"/>
      <!-- fax / printer -->
      <rect x="507" y="1138" width="16" height="6"/>
      <rect x="503" y="1145" width="24" height="11" rx="2"/>
      <rect x="508" y="1152" width="14" height="9" fill="var(--paper)" stroke="var(--ink)" stroke-width="2"/>
    </g>
  </svg>

  <p class="cta">For Appointment</p>
  <p class="contact-line contact-address">4410 Linden Ave.<br>Maple Grove, CA, 90000</p>
  <p class="contact-line contact-phone">(555) 014-2200</p>
  <p class="contact-line contact-fax">(555) 014-2207</p>
</main>
</body>
</html>
```